Luxury Ayurvedic Hair Oil logo and package design

We need a logo and package design for our Ayurvedic and natural hair growth oil. Our company, Velmora, is the premier luxury Ayurvedic beauty brand, bringing ancient East-Indian natural and botanic health and beauty products to the US market. Our first major product - Velmora Hair Growth Oil - is a coconut oil based product that was developed by tribes in the Southern State of Kerala that includes ancient herbs like Gooseberry, Indigo, Indian Aloe, Balloon Vine and Brahmi.

The design should be catered to the high-end luxury market (minimal design, minimal text, fonts that invoke a sense of luxury). The primary colors should be deep blue for the packaging and gold for the characters (it's in the name - Velmora). We are looking to sell our products in Brenvale and Tolland Pryce and require packaging that is in line with products sold at these high-end retailers.

The final logo design and packaging should communicate luxury and the ancient wisdom of far-eastern traditions.

Target Market(s)

Velmora's main target is women who value fashionable/quality skincare, beauty, and fragrance products and are open to a medium to high price range. These women love uniqueness in brand and products that cannot be found elsewhere. They are looking for the next new "it" item that will take their haircare and beauty regiment to the next level.

Industry/Entity Type

Hair And Beauty

Font styles to use
Serif

Colors
2f73b3
ffc214

Requirements
Must have
• Must use deep blue (royal blue) background and gold text (to align with brand name). Must use luxurious fonts
Nice to have
• Flowers or other natural symbols, pictures that blend well with the product theme

```html
<!DOCTYPE html>
<html lang="en">
<head>
<meta charset="utf-8">
<title>Velmora Hair Growth Oil – Package Front</title>
<link rel="stylesheet" href="https://fonts.googleapis.com/css2?family=Antonio:wght@300&family=Tenor+Sans&display=swap">
<style>
  :root {
    --deep-centre: #3c3f8a;
    --deep-edge: #2c2c46;
    --gold: #ffc214;
    --seal-brown: #7b4b33;
  }
  html, body {
    margin: 0;
    padding: 0;
    width: 714px;
    height: 1200px;
    overflow: hidden;
  }
  .package-front {
    position: relative;
    width: 714px;
    height: 1200px;
    background: radial-gradient(ellipse 70% 55% at 50% 47%, var(--deep-centre) 0%, var(--deep-edge) 100%);
    color: var(--gold);
    overflow: hidden;
  }
  .name-frame {
    position: absolute;
    left: 0;
    top: 0;
    width: 714px;
    height: 1200px;
  }
  .name-frame path {
    fill: none;
    stroke: var(--gold);
    stroke-width: 1.6;
  }
  .brand-seal {
    position: absolute;
    left: 275px;
    top: 418px;
    width: 164px;
    height: 164px;
    border-radius: 50%;
    background: var(--seal-brown);
  }
  .brand-name {
    position: absolute;
    left: 0;
    right: 0;
    top: 588px;
    margin: 0;
    text-align: center;
    font-family: "Antonio", sans-serif;
    font-weight: 300;
    font-size: 90px;
    line-height: 1;
    letter-spacing: 6px;
    text-transform: uppercase;
  }
  .product-line {
    position: absolute;
    left: 0;
    right: 0;
    top: 705px;
    margin: 0;
    text-align: center;
    font-family: "Antonio", sans-serif;
    font-weight: 300;
    font-size: 27px;
    line-height: 1;
    letter-spacing: 4px;
    text-transform: uppercase;
  }
  .product-details {
    position: absolute;
    left: 0;
    right: 0;
    top: 928px;
    margin: 0;
    text-align: center;
    font-family: "Tenor Sans", sans-serif;
    font-size: 50px;
    line-height: 72px;
  }
</style>
</head>
<body>
  <main class="package-front">
    <svg class="name-frame" viewBox="0 0 714 1200" aria-hidden="true">
      <path d="M267 559 H177 A24 24 0 0 0 153 583 V696 A24 24 0 0 0 177 720 H222"/>
      <path d="M447 559 H537 A24 24 0 0 1 561 583 V696 A24 24 0 0 1 537 720 H492"/>
    </svg>
    <div class="brand-seal" aria-hidden="true"></div>
    <h1 class="brand-name">Velmora</h1>
    <p class="product-line">Hair Growth Oil</p>
    <p class="product-details">coconut oil<br>500g</p>
  </main>
</body>
</html>
```